Business Card Design

We need a business card designed to the point of print ready to take to our printers. the design should be professional, easy to read and simple. The cards should represent our business as professional and trust worthy.

Attached are several versions o the logo, and also the details for the card to be printed. please do communicate if different versions of the logo is required.

Industry/Entity Type

Business

```html
<!DOCTYPE html>
<html lang="en">
<head>
<meta charset="utf-8">
<title>CashReach Pty Ltd – Business Card</title>
<link rel="stylesheet" href="https://fonts.googleapis.com/css2?family=Mulish:wght@400;700;800&display=swap">
<style>
  :root {
    --bg: #d9d6d0;
    --card: #111111;
    --card-edge: #1c1c1c;
    --white: #ffffff;
    --muted: #d8d8d8;
    --logo-grey: #8f8f8f;
    --orange: #f39a0f;
    --band-shadow: #4a4a4a;
    --web-text: #3a2a08;
  }
  * { margin: 0; padding: 0; box-sizing: border-box; }
  html, body { width: 1200px; height: 871px; overflow: hidden; }
  body {
    background: var(--bg);
    font-family: "Mulish", Arial, sans-serif;
    position: relative;
  }
  .card {
    position: absolute;
    width: 560px;
    height: 320px;
    background: linear-gradient(160deg, var(--card-edge), var(--card) 60%);
    box-shadow: 0 14px 30px rgba(0,0,0,.35);
    overflow: hidden;
  }
  .card--back { left: 120px; top: 100px; }
  .card--front { left: 520px; top: 450px; }

  .brand { position: absolute; color: var(--logo-grey); font-weight: 800; line-height: 1; }
  .brand__name { display: block; }
  .brand__suffix { display: block; text-align: right; font-size: .42em; margin-top: 4px; }
  .card--back .brand { left: 130px; top: 112px; font-size: 58px; }
  .card--front .brand { right: 40px; top: 44px; font-size: 44px; }

  .holder { position: absolute; left: 40px; top: 108px; color: var(--white); }
  .holder__name { font-size: 19px; font-weight: 700; }
  .holder__title { font-size: 12px; color: var(--muted); margin-top: 4px; }

  .contact { position: absolute; left: 40px; top: 168px; font-size: 13px; color: var(--muted); }
  .contact__address { margin-bottom: 8px; }
  .contact__row { display: flex; gap: 28px; line-height: 1.55; }
  .contact__label { width: 48px; color: var(--orange); font-weight: 700; }

  .footer-band { position: absolute; left: 0; bottom: 0; width: 560px; height: 60px; }
  .website {
    position: absolute; right: 24px; bottom: 17px;
    font-size: 13px; color: var(--web-text); font-weight: 700;
  }
</style>
</head>
<body>
  <section class="card card--back" aria-label="Card back">
    <div class="brand">
      <span class="brand__name">CashReach</span>
      <span class="brand__suffix">Pty Ltd</span>
    </div>
  </section>

  <section class="card card--front" aria-label="Card front">
    <div class="brand">
      <span class="brand__name">CashReach</span>
      <span class="brand__suffix">Pty Ltd</span>
    </div>

    <div class="holder">
      <p class="holder__name">Dana Whitlow</p>
      <p class="holder__title">Managing Director</p>
    </div>

    <div class="contact">
      <p class="contact__address">PO Box 7720 Harbour Plaza Qld 4305</p>
      <p class="contact__row"><span class="contact__label">phone</span><span>+61 400 555 019</span></p>
      <p class="contact__row"><span class="contact__label">email</span><span>dwhitlow@cashreach.com.au</span></p>
    </div>

    <svg class="footer-band" viewBox="0 0 560 60" aria-hidden="true">
      <polygon points="0,24 325,24 345,6 560,6 560,12 348,12 328,30 0,30" fill="var(--band-shadow)"/>
      <polygon points="0,30 328,30 348,12 560,12 560,52 0,52 0,44 0,38" fill="var(--orange)"/>
      <polygon points="0,38 332,38 340,30 340,52 0,52" fill="var(--card)"/>
    </svg>
    <p class="website">www.cashreach.com.au</p>
  </section>
</body>
</html>
```